Staffing/Recruitment company

We need to upgrade our website. At the moment we have a template that was built last year and looks not good at all.
We would like to update it with a new design based on what is popular this year. Including some visual effects etc.
This website is to give all information to our potential clients about what we do, clients with worked in the past, how to contact us and about us.
The website consists of 4 pages.
We would like to see a design that uses the color blue.
The current website is https://brightkelvo.us/
Logo of the company is uploaded

Some designs were not complete...

```html
<!DOCTYPE html>
<html lang="en">
<head>
<meta charset="utf-8">
<title>Kelvo Systems — Staffing &amp; QA Talent</title>
<link href="https://fonts.googleapis.com/css2?family=Montserrat:wght@500;600;700;800&family=Poppins:wght@400;500;600&display=swap" rel="stylesheet">
<style>
:root{
  --navy:#0e1a3a;
  --navy-deep:#0b1024;
  --orange:#f15a24;
  --orange-soft:#f47a3f;
  --ink:#1c1c1c;
  --body:#444a55;
  --muted:#f3f4f7;
  --line:#e3e5ea;
  --white:#ffffff;
}
*{box-sizing:border-box;margin:0;padding:0}
html,body{width:1200px;height:4532px;overflow:hidden}
body{font-family:"Poppins",sans-serif;color:var(--body);background:var(--white);position:relative}
h1,h2,h3,h4{font-family:"Montserrat",sans-serif;color:var(--ink)}
.btn{display:inline-block;background:var(--orange);color:var(--white);font-family:"Montserrat",sans-serif;font-weight:700;font-size:15px;letter-spacing:.5px;padding:12px 28px;text-transform:uppercase}
.btn--navy{background:var(--navy)}
.photo{position:absolute}

/* top bar */
.topbar{position:absolute;top:0;left:0;width:1200px;height:48px;background:var(--navy);color:var(--white);font-size:14px;display:flex;align-items:center;padding:0 100px}
.topbar span{margin-right:28px;display:flex;align-items:center;gap:8px}
.topbar .social{margin-left:auto;display:flex;gap:8px}
.dot{width:22px;height:22px;border:1.5px solid var(--white);border-radius:50%}

/* nav */
.nav{position:absolute;top:48px;left:0;width:1200px;height:72px;display:flex;align-items:center;padding:0 100px}
.brand{display:flex;align-items:center;gap:10px;font-family:"Montserrat",sans-serif;font-weight:800;font-size:20px;color:var(--navy);text-transform:uppercase}
.brand i{width:30px;height:30px;background:var(--orange);display:block}
.menu{margin-left:auto;display:flex;gap:38px;font-family:"Montserrat",sans-serif;font-weight:600;font-size:15px;color:var(--navy)}
.menu .active{color:var(--orange)}

/* hero */
.hero{position:absolute;top:120px;left:0;width:1200px;height:612px;background:linear-gradient(100deg,#e9ecef 0%,#f4f1ec 45%,#c7ad8c 80%,#9c8a74 100%)}
.hero h1{position:absolute;left:100px;top:226px;font-size:56px;line-height:1.08;font-weight:800;color:var(--navy);width:560px}
.hero .btn{position:absolute;left:100px;top:372px}
.hero .pager{position:absolute;left:560px;bottom:28px;display:flex;gap:8px}
.hero .pager b{width:10px;height:10px;border-radius:50%;background:#fff;opacity:.6}
.hero .pager b:first-child{opacity:1;background:var(--orange)}

/* about */
.about-art{left:100px;top:780px;width:460px;height:520px;background:linear-gradient(135deg,#e8ebf3,#f7ece5)}
.about-text{position:absolute;left:660px;top:790px;width:500px}
.about-text h2{font-size:52px;font-weight:800;color:var(--navy);margin-bottom:28px}
.about-text h2 em,.section-title em{font-style:normal;color:var(--orange)}
.about-text p{font-size:16px;line-height:1.55}
.about-text .btn{margin-top:40px}

/* what we do */
.section-title{position:absolute;left:0;width:1200px;text-align:center;font-size:46px;font-weight:800;color:var(--navy)}
.service{position:absolute;width:440px}
.service h3{font-size:21px;font-weight:700;line-height:1.3;text-transform:uppercase;margin-bottom:20px}
.service p{font-size:15px;line-height:1.55;margin-bottom:26px}
.icon-badge{position:absolute;width:96px;height:96px;border-radius:50%;display:flex;align-items:center;justify-content:center;border:6px solid #fff}

/* divisions */
.divisions{position:absolute;top:2760px;left:0;width:1200px;height:560px;background:var(--muted)}
.cards{position:absolute;top:148px;left:100px;display:flex;gap:12px}
.card{width:243px;height:324px;background:var(--white);box-shadow:0 4px 14px rgba(0,0,0,.08);text-align:center;display:flex;flex-direction:column}
.card .thumb{height:172px;flex:none}
.card h4{font-size:17px;font-weight:700;margin:16px 0 6px}
.card p{font-size:12.5px;line-height:1.45;padding:0 18px}
.card a{font-family:"Montserrat",sans-serif;font-size:12px;font-weight:700;color:var(--orange);text-decoration:underline;margin-top:auto;margin-bottom:16px}

/* clients */
.clients-row{position:absolute;top:3472px;left:100px;width:1000px;display:flex;gap:18px}
.client{width:186px;height:120px;border:1px solid var(--line);display:flex;align-items:center;justify-content:center;gap:10px;font-family:"Montserrat",sans-serif;font-weight:700;font-size:20px;color:#3a3f4a}
.client i{width:22px;height:22px;border-radius:50%;background:#3a3f4a;display:block}
.arrow{position:absolute;top:3518px}

/* career */
.career{position:absolute;top:3688px;left:0;width:1200px;height:512px;background:linear-gradient(120deg,var(--orange) 0%,var(--orange-soft) 100%)}
.career-photo{left:100px;top:-60px;width:480px;height:572px;background:linear-gradient(180deg,#f4b13a 0%,#e89a2a 50%,#3a3f4f 100%)}
.career-text{position:absolute;left:660px;top:100px;width:460px;color:var(--white)}
.career-text h2{color:var(--white);font-size:38px;font-weight:800;line-height:1.15;text-transform:uppercase;margin-bottom:22px}
.career-text p{font-size:16px;line-height:1.55;margin-bottom:30px}

/* footer */
.footer{position:absolute;top:4200px;left:0;width:1200px;height:332px;background:var(--navy-deep);color:#cfd3de}
.footer .brand{position:absolute;left:100px;top:64px;color:var(--white);font-size:26px}
.footer .social{position:absolute;left:100px;top:140px;display:flex;gap:10px}
.footer .social .dot{width:38px;height:38px;border:none;background:var(--white)}
.fcol{position:absolute;top:64px;font-size:14px;line-height:1.9}
.fcol h5{font-family:"Montserrat",sans-serif;color:var(--white);font-size:15px;font-weight:700;margin-bottom:10px;text-transform:uppercase}
.fcol .row{display:flex;align-items:center;gap:12px;margin-bottom:8px}
.fcol .ic{width:30px;height:30px;border-radius:50%;background:var(--orange);display:flex;align-items:center;justify-content:center}
.copy{position:absolute;left:100px;right:100px;bottom:0;height:54px;border-top:1px solid #2a3150;text-align:center;line-height:54px;font-size:13px}
</style>
</head>
<body>

<header class="topbar">
  <span>
    <svg width="14" height="14" viewBox="0 0 24 24" fill="#fff"><path d="M6.6 10.8a15.1 15.1 0 0 0 6.6 6.6l2.2-2.2a1 1 0 0 1 1-.25 11.4 11.4 0 0 0 3.6.57 1 1 0 0 1 1 1V20a1 1 0 0 1-1 1A17 17 0 0 1 3 4a1 1 0 0 1 1-1h3.5a1 1 0 0 1 1 1c0 1.25.2 2.45.57 3.6a1 1 0 0 1-.25 1z"/></svg>
    +1 555-010-2040</span>
  <span>
    <svg width="15" height="12" viewBox="0 0 24 18" fill="none" stroke="#fff" stroke-width="2"><rect x="1" y="1" width="22" height="16"/><path d="M1 1l11 9 11-9"/></svg>
    info@brightkelvo.us</span>
  <div class="social"><i class="dot"></i><i class="dot"></i><i class="dot"></i><i class="dot"></i></div>
</header>

<nav class="nav">
  <div class="brand"><i></i>Kelvo Systems</div>
  <div class="menu"><span class="active">HOME</span><span>SERVICES</span><span>CLIENTS</span><span>ABOUT US</span><span>CONTACT US</span></div>
</nav>

<section class="hero" role="img" aria-label="Hand stacking wooden blocks printed with people icons into a pyramid, one highlighted candidate at the top">
  <h1>HOW SOON CAN<br>YOU START?</h1>
  <span class="btn">Get Started</span>
  <div class="pager"><b></b><b></b><b></b></div>
</section>

<div class="photo about-art" role="img" aria-label="Large decorative company emblem in navy and orange"></div>
<section class="about-text">
  <h2>ABOUT <em>US</em></h2>
  <p>Day in and day out for the last years we've been more than just a staffing company. Throughout this time we've built relationships, we've grown together internally and externally, and have created a system that allows us to personally cater to the needs of our clients &amp; candidates. We've been a mentor for some, a team builder for others, but most importantly we've been there. We know there is no substitute for experience, so let us help you navigate through the ever-changing web of talent.</p>
  <span class="btn">Learn More</span>
</section>

<h2 class="section-title" style="top:1376px">WHAT <em>WE DO</em></h2>

<section class="service" style="left:100px;top:1520px">
  <h3>Hire top professional<br>SDETs</h3>
  <p>We work with elite test-automation engineers. As a network, we have a very rigorous screening process to identify the best. We are experts in our domains, and we look for great problem solvers with passion and drive — the types of people we want to work.</p>
  <span class="btn">Learn More</span>
</section>
<div class="photo" style="left:600px;top:1472px;width:500px;height:288px;background:linear-gradient(135deg,#2c4a7a,#6a86b4 60%,#b9c6dc)" role="img" aria-label="Engineer working on a laptop at a desk"></div>
<div class="icon-badge" style="left:552px;top:1632px;background:var(--navy)">
  <svg width="44" height="44" viewBox="0 0 44 44" fill="none" stroke="#fff" stroke-width="2.5"><rect x="6" y="8" width="32" height="22" rx="2"/><path d="M15 38h14M22 30v8"/></svg>
</div>

<div class="photo" style="left:100px;top:1872px;width:500px;height:400px;background:linear-gradient(135deg,#e9ecf1,#c9d2de 60%,#8a98ad)" role="img" aria-label="Trainer presenting charts on a whiteboard to a team"></div>
<div class="icon-badge" style="left:552px;top:2024px;background:var(--orange)">
  <svg width="44" height="44" viewBox="0 0 44 44" fill="none" stroke="#fff" stroke-width="2.5"><circle cx="22" cy="22" r="8"/><path d="M22 4v8M22 32v8M4 22h8M32 22h8"/></svg>
</div>
<section class="service" style="left:700px;top:1960px">
  <h3>Let us build end to end<br>automated QA infrastructure</h3>
  <p>We can safe your time and budget. Our team will build end to end automated QA infrastructure for you. We work with latest technologies and tools (Quarkium, Protrax, Jaspen, Cukeline, Karvo).</p>
  <span class="btn">Learn More</span>
</section>

<section class="service" style="left:100px;top:2320px">
  <h3>Request instructor for<br>your team</h3>
  <p>We are committed to helping companies find the best instructors. Kelvo Systems has been successful in helping to connect many companies with top tutors, and a key component of this success is our thorough screening &amp; qualification process.</p>
  <span class="btn">Learn More</span>
</section>
<div class="photo" style="left:600px;top:2272px;width:500px;height:400px;background:linear-gradient(135deg,#d8dde4,#eef0f2 50%,#9aa3ae)" role="img" aria-label="Team meeting around a conference table"></div>
<div class="icon-badge" style="left:552px;top:2424px;background:var(--navy)">
  <svg width="44" height="44" viewBox="0 0 44 44" fill="none" stroke="#fff" stroke-width="2.5"><circle cx="22" cy="15" r="7"/><path d="M8 38c2-8 8-12 14-12s12 4 14 12"/></svg>
</div>

<section class="divisions">
  <h2 class="section-title" style="top:88px">OUR <em>DIVISIONS</em></h2>
  <div class="cards">
    <article class="card">
      <div class="thumb" style="background:linear-gradient(135deg,#0d3a78,#3f8fd6)" role="img" aria-label="Glass office towers"></div>
      <h4>Finance</h4>
      <p>With Wall Street's fast-paced dynamic &amp; ever changing environment, business</p>
      <a>LEARN MORE</a>
    </article>
    <article class="card">
      <div class="thumb" style="background:linear-gradient(135deg,#1d2a3c,#4f6a86)" role="img" aria-label="Developers at computer screens"></div>
      <h4>Information Technology</h4>
      <p>The technology of today is not going to be the technology of tomorrow, and keeping up.</p>
      <a>LEARN MORE</a>
    </article>
    <article class="card">
      <div class="thumb" style="background:linear-gradient(135deg,#2b5c8a,#9fc3dc)" role="img" aria-label="Medical staff in a clinic"></div>
      <h4>Healthcare</h4>
      <p>Not only do we provide services to the finance and technology world, we also serve.</p>
      <a>LEARN MORE</a>
    </article>
    <article class="card">
      <div class="thumb" style="background:linear-gradient(135deg,#c9b89a,#efe6d4)" role="img" aria-label="Columns of a government building"></div>
      <h4>Government Projects</h4>
      <p>Navigating the rules and regulations of Government integrators isn't always easy.</p>
      <a>LEARN MORE</a>
    </article>
  </div>
</section>

<h2 class="section-title" style="top:3390px">OUR <em>CLIENTS</em></h2>
<svg class="arrow" style="left:52px" width="24" height="30" viewBox="0 0 24 30"><path d="M18 3L6 15l12 12" fill="none" stroke="#555" stroke-width="3"/></svg>
<div class="clients-row">
  <div class="client"><i></i>Northvale</div>
  <div class="client"><i></i>Brixton</div>
  <div class="client"><i></i>Orlean</div>
  <div class="client"><i></i>Calvero</div>
  <div class="client"><i></i>Temora</div>
</div>
<svg class="arrow" style="left:1124px" width="24" height="30" viewBox="0 0 24 30"><path d="M6 3l12 12L6 27" fill="none" stroke="#555" stroke-width="3"/></svg>

<section class="career">
  <div class="photo career-photo" role="img" aria-label="Smiling woman in a yellow sweater holding a laptop"></div>
  <div class="career-text">
    <h2>Join our career<br>network</h2>
    <p>Our Career Network will enhance your job search and application process. Whether you choose to apply or just leave your information, we look forward to staying connected with you.</p>
    <span class="btn btn--navy">Join Now</span>
  </div>
</section>

<footer class="footer">
  <div class="brand"><i></i>Kelvo Systems</div>
  <div class="social"><i class="dot"></i><i class="dot"></i><i class="dot"></i><i class="dot"></i></div>
  <div class="fcol" style="left:510px">
    <h5>Quick Links</h5>
    Home<br>Services<br>Clients<br>About Us<br>Contact Us
  </div>
  <div class="fcol" style="left:696px">
    <h5>Contact Info</h5>
    <div class="row"><span class="ic"><svg width="14" height="14" viewBox="0 0 24 24" fill="#fff"><path d="M12 2a7 7 0 0 0-7 7c0 5 7 13 7 13s7-8 7-13a7 7 0 0 0-7-7zm0 9.5A2.5 2.5 0 1 1 12 6.5a2.5 2.5 0 0 1 0 5z"/></svg></span>2140 Linden Ave, Oakmont, VA</div>
    <div class="row"><span class="ic"><svg width="13" height="13" viewBox="0 0 24 24" fill="#fff"><path d="M6.6 10.8a15.1 15.1 0 0 0 6.6 6.6l2.2-2.2a1 1 0 0 1 1-.25 11.4 11.4 0 0 0 3.6.57 1 1 0 0 1 1 1V20a1 1 0 0 1-1 1A17 17 0 0 1 3 4a1 1 0 0 1 1-1h3.5a1 1 0 0 1 1 1c0 1.25.2 2.45.57 3.6a1 1 0 0 1-.25 1z"/></svg></span>+1 555-010-2040</div>
    <div class="row"><span class="ic"><svg width="14" height="11" viewBox="0 0 24 18" fill="none" stroke="#fff" stroke-width="2.4"><rect x="1" y="1" width="22" height="16"/><path d="M1 1l11 9 11-9"/></svg></span>info@brightkelvo.us</div>
  </div>
  <div class="fcol" style="left:984px">
    <h5>More</h5>
    Privacy policy<br>Terms and conditions<br>Sitemap<br>Help
  </div>
  <div class="copy">Copyright © 2022 Kelvo Systems, LLC. All rights reserved.</div>
</footer>

</body>
</html>
```